Tidal Pines - explore habits of productive people

Tidal Pines is a social place around habits and productivity

The full brief below:

https://docs.quorvane.net/document/d/7Rt-PWMZXK4ubEhqNcs-V2Ytm9Gx8KdfHzJqBsQwnyrT/edit?usp=sharing

Colors

Designer to choose colors to be used in the design.

Requirements
Must have
• - a feed page to display habits
• - a habit page to add a habit
• / clean, no cluttered design, lots of white space
• / inspired by lattice design or other design system
Nice to have
• - user page

```html
<!DOCTYPE html>
<html lang="en">
<head>
<meta charset="utf-8">
<title>Tidal Pines – Feed and Add Habit</title>
<link rel="stylesheet" href="https://fonts.googleapis.com/css2?family=Poppins:wght@400;500;600;700&display=swap">
<style>
  :root {
    --bg: #fff5f2;
    --screen-body: #f4f4f4;
    --surface: #ffffff;
    --accent: #ff8a5b;
    --accent-soft: #ffb494;
    --ink: #3f3f3f;
    --ink-strong: #2f2f2f;
    --muted: #9a9a9a;
    --icon: #a7a7a7;
    --line: #cfcfcf;
    --good-bg: #d8f6ea;
    --good-ink: #27c483;
    --heart-on: #f25a5a;
    --avatar-dark: #2c2f36;
    --avatar-light: #d9d2cc;
  }
  * { box-sizing: border-box; margin: 0; padding: 0; }
  html, body { width: 1200px; height: 1200px; overflow: hidden; }
  body { background: var(--bg); font-family: "Poppins", sans-serif; color: var(--ink); position: relative; }

  .screen { position: absolute; top: 86px; width: 400px; background: var(--screen-body); overflow: hidden; }
  .screen--feed { left: 181px; height: 1027px; }
  .screen--add { left: 619px; height: 884px; }

  .app-header { position: absolute; left: 0; top: 0; width: 100%; height: 104px; background: var(--surface); }
  .status-time { position: absolute; left: 37px; top: 17px; font-size: 16px; font-weight: 600; color: var(--ink-strong); line-height: 20px; }
  .status-icons { position: absolute; right: 16px; top: 18px; }
  .brand { position: absolute; left: 20px; top: 57px; font-size: 28px; font-weight: 500; color: var(--ink-strong); letter-spacing: 0.5px; line-height: 36px; }
  .header-bell { position: absolute; left: 306px; top: 62px; }
  .header-avatar { position: absolute; left: 348px; top: 60px; width: 30px; height: 30px; border-radius: 50%; background: var(--avatar-dark); }

  .card { position: absolute; left: 21px; width: 357px; background: var(--surface); border-radius: 4px; }
  .tag-good { position: absolute; left: 27px; height: 20px; width: 48px; background: var(--good-bg); color: var(--good-ink); border-radius: 2px; font-size: 10px; font-weight: 600; line-height: 20px; text-align: center; }
  .heart { position: absolute; right: 26px; }
  .label { position: absolute; left: 27px; font-size: 15px; font-weight: 500; color: var(--accent); line-height: 20px; }
  .habit-title { position: absolute; left: 27px; font-size: 15px; font-weight: 500; color: var(--ink); line-height: 20px; }
  .toggle { position: absolute; right: 27px; font-size: 12px; font-weight: 600; color: var(--accent); line-height: 16px; display: flex; align-items: center; gap: 6px; }
  .loop-step { position: absolute; left: 27px; width: 310px; font-size: 11px; line-height: 17.5px; color: var(--muted); letter-spacing: 0.2px; }
  .loop-step b { font-weight: 600; color: var(--ink); }
  .author { position: absolute; left: 27px; display: flex; align-items: center; gap: 11px; font-size: 12px; font-weight: 500; color: var(--ink); }
  .author-avatar { width: 24px; height: 24px; border-radius: 50%; }
  .author-avatar--light { background: var(--avatar-light); }
  .author-avatar--dark { background: var(--avatar-dark); }

  .bottom-nav { position: absolute; left: 0; width: 100%; height: 65px; background: var(--surface); }
  .nav-icon { position: absolute; top: 50%; transform: translate(-50%, -50%); }
  .nav-add { position: absolute; top: 50%; width: 42px; height: 42px; margin-top: -21px; margin-left: -21px; border-radius: 50%; background: var(--accent); box-shadow: 0 4px 10px rgba(255,138,91,0.35); display: flex; align-items: center; justify-content: center; }

  .form-title { position: absolute; left: 27px; top: 28px; font-size: 19px; font-weight: 600; color: var(--accent); line-height: 24px; }
  .type-row { position: absolute; left: 27px; top: 95px; display: flex; align-items: center; font-size: 13px; line-height: 20px; }
  .type-row .type-label { font-weight: 600; color: var(--ink); font-size: 14px; margin-right: 18px; }
  .radio { display: flex; align-items: center; gap: 6px; color: var(--ink); margin-right: 14px; }
  .radio-dot { width: 12px; height: 12px; border-radius: 50%; border: 1px solid var(--muted); position: relative; }
  .radio-dot--on { border-color: var(--accent); }
  .radio-dot--on::after { content: ""; position: absolute; left: 2px; top: 2px; width: 6px; height: 6px; border-radius: 50%; background: var(--accent); }
  .field { position: absolute; left: 27px; width: 302px; height: 47px; border: 1px solid var(--line); border-radius: 3px; font-size: 15px; color: #a9a9a9; line-height: 45px; padding-left: 31px; }
  .field--active { border-color: var(--accent); height: 47px; font-size: 13px; color: var(--ink); padding-left: 31px; }
  .field-legend { position: absolute; left: 23px; top: -10px; padding: 0 8px; background: var(--surface); color: var(--accent); font-size: 14px; line-height: 18px; }
  .section-label { position: absolute; left: 28px; top: 231px; font-size: 14px; font-weight: 500; color: var(--ink); line-height: 20px; }
  .btn-primary { position: absolute; left: 27px; top: 570px; width: 146px; height: 42px; background: var(--accent); color: #fff; font-size: 14px; font-weight: 600; line-height: 42px; text-align: center; border-radius: 2px; box-shadow: 0 3px 8px rgba(255,138,91,0.3); }
</style>
</head>
<body>

<svg width="0" height="0" style="position:absolute">
  <defs>
    <symbol id="i-signal" viewBox="0 0 16 10"><rect x="0" y="7" width="3" height="3" rx="0.5"/><rect x="4" y="5" width="3" height="5" rx="0.5"/><rect x="8" y="2.5" width="3" height="7.5" rx="0.5"/><rect x="12" y="0" width="3" height="10" rx="0.5"/></symbol>
    <symbol id="i-wifi" viewBox="0 0 16 12"><path d="M8 11.5 5.6 9a3.4 3.4 0 0 1 4.8 0Z"/><path d="M3.5 7 2.2 5.6a8.2 8.2 0 0 1 11.6 0L12.5 7a6.3 6.3 0 0 0-9 0Z"/><path d="M1.3 4.6 0 3.2a11.3 11.3 0 0 1 16 0l-1.3 1.4a9.4 9.4 0 0 0-13.4 0Z"/></symbol>
    <symbol id="i-battery" viewBox="0 0 24 11"><rect x="0" y="0" width="21" height="11" rx="2.5"/><rect x="22" y="3.5" width="2" height="4" rx="1"/></symbol>
    <symbol id="i-heart" viewBox="0 0 24 22"><path d="M12 21.5 10.3 20C4.2 14.4 0 10.7 0 6.2 0 2.6 2.8 0 6.4 0c2 0 4.1.9 5.6 2.5C13.5.9 15.6 0 17.6 0 21.2 0 24 2.6 24 6.2c0 4.5-4.2 8.2-10.3 13.8Z"/></symbol>
    <symbol id="i-compass" viewBox="0 0 26 26"><circle cx="13" cy="13" r="13"/><path d="M18.5 7.5 15 15l-7.5 3.5L11 11Z" fill="#fff"/><circle cx="13" cy="13" r="1.6"/></symbol>
    <symbol id="i-book" viewBox="0 0 20 26"><path d="M2 0h16a2 2 0 0 1 2 2v22a2 2 0 0 1-2 2H2a2 2 0 0 1-2-2V2a2 2 0 0 1 2-2Z"/><path d="M5 0h6v10l-3-2-3 2Z" fill="#fff"/></symbol>
    <symbol id="i-gear" viewBox="0 0 26 26"><circle cx="13" cy="13" r="9"/><circle cx="13" cy="13" r="11" fill="none" stroke="currentColor" stroke-width="4" stroke-dasharray="4.3 4.3"/><circle cx="13" cy="13" r="4" fill="#fff"/></symbol>
    <symbol id="i-bell" viewBox="0 0 20 24"><path d="M10 2a1.5 1.5 0 0 1 1.5 1.5v.7A6.5 6.5 0 0 1 16.5 10.5v5.5l2 2.5v1H1.5v-1l2-2.5v-5.5a6.5 6.5 0 0 1 5-6.3v-.7A1.5 1.5 0 0 1 10 2Z"/><path d="M7.5 21h5a2.5 2.5 0 0 1-5 0Z"/></symbol>
  </defs>
</svg>

<!-- Feed screen -->
<section class="screen screen--feed" aria-label="Habit feed">
  <header class="app-header">
    <span class="status-time">4:08</span>
    <span class="status-icons" style="display:flex;gap:6px;align-items:center;fill:var(--ink-strong)">
      <svg width="18" height="11"><use href="#i-signal"/></svg>
      <svg width="16" height="12"><use href="#i-wifi"/></svg>
      <svg width="24" height="11"><use href="#i-battery"/></svg>
    </span>
    <span class="brand">TIDAL PINES</span>
    <span class="header-bell">
      <svg width="22" height="26" viewBox="0 0 22 26" style="fill:var(--icon)"><use href="#i-bell" width="20" height="24" y="2"/><circle cx="17" cy="6" r="3" fill="var(--accent)"/></svg>
    </span>
    <span class="header-avatar" role="img" aria-label="Profile photo of the signed-in user"></span>
  </header>

  <article class="card" style="top:136px;height:536px">
    <span class="tag-good" style="top:28px">Good</span>
    <svg class="heart" style="top:29px;fill:var(--heart-on)" width="20" height="18"><use href="#i-heart"/></svg>
    <span class="label" style="top:65px">Habit</span>
    <h2 class="habit-title" style="top:94px">Workout Every Morning Before Work</h2>
    <span class="toggle" style="top:132px">
      <svg width="10" height="7" viewBox="0 0 10 7" fill="none" stroke="currentColor" stroke-width="1.6"><path d="M1 6l4-4 4 4"/></svg>Less
    </span>
    <span class="label" style="top:167px">Loop</span>
    <p class="loop-step" style="top:195px"><b>Cue:</b> Put your gym clothes where they are clearly visible in your closet.</p>
    <p class="loop-step" style="top:242px"><b>Craving:</b> Follow a simple workout routine that's fun and efficient that fits within your schedule.</p>
    <p class="loop-step" style="top:289px"><b>Response:</b> Train at home, or choose a gym that is close to the house or your work place.</p>
    <p class="loop-step" style="top:335px"><b>Reward:</b> Log the workout in your journal or calendar. Progress makes you feel good, it's a reward.</p>
    <span class="toggle" style="top:412px">
      <svg width="13" height="13" viewBox="0 0 13 13" fill="currentColor"><path d="M0 10.5V13h2.5l7.4-7.4-2.5-2.5Z"/><path d="M12.8 2.7 10.3.2a.7.7 0 0 0-1 0L8.2 1.3l2.5 2.5 1.1-1.1a.7.7 0 0 0 0-1Z"/></svg>Contribute
    </span>
    <span class="label" style="top:452px">Author</span>
    <div class="author" style="top:485px">
      <span class="author-avatar author-avatar--light" role="img" aria-label="Author portrait"></span>Maren Holt
    </div>
  </article>

  <article class="card" style="top:688px;height:241px">
    <span class="tag-good" style="top:28px">Good</span>
    <svg class="heart" style="top:30px;fill:var(--icon)" width="20" height="18"><use href="#i-heart"/></svg>
    <span class="label" style="top:66px">Habit</span>
    <h2 class="habit-title" style="top:94px">Reading One Book a Week</h2>
    <span class="label" style="top:133px">Author</span>
    <div class="author" style="top:166px">
      <span class="author-avatar author-avatar--dark" role="img" aria-label="Author portrait"></span>Ilan Brooks
    </div>
    <span class="toggle" style="top:197px">
      <svg width="10" height="7" viewBox="0 0 10 7" fill="none" stroke="currentColor" stroke-width="1.6"><path d="M1 1l4 4 4-4"/></svg>More
    </span>
  </article>

  <nav class="bottom-nav" style="top:962px">
    <svg class="nav-icon" style="left:36px;fill:var(--accent)" width="26" height="26"><use href="#i-compass"/></svg>
    <svg class="nav-icon" style="left:118px;fill:var(--icon)" width="20" height="26"><use href="#i-book"/></svg>
    <span class="nav-add" style="left:199px"><svg width="20" height="20" viewBox="0 0 20 20" stroke="#fff" stroke-width="2.4" stroke-linecap="round"><path d="M10 2v16M2 10h16"/></svg></span>
    <svg class="nav-icon" style="left:282px;fill:var(--icon)" width="26" height="24"><use href="#i-heart"/></svg>
    <svg class="nav-icon" style="left:363px;fill:var(--icon);color:var(--icon)" width="26" height="26"><use href="#i-gear"/></svg>
  </nav>
</section>

<!-- Add habit screen -->
<section class="screen screen--add" aria-label="Add a habit">
  <header class="app-header">
    <span class="status-time">4:08</span>
    <span class="status-icons" style="display:flex;gap:6px;align-items:center;fill:var(--ink-strong)">
      <svg width="18" height="11"><use href="#i-signal"/></svg>
      <svg width="16" height="12"><use href="#i-wifi"/></svg>
      <svg width="24" height="11"><use href="#i-battery"/></svg>
    </span>
    <span class="brand">TIDAL PINES</span>
    <span class="header-bell">
      <svg width="22" height="26" viewBox="0 0 22 26" style="fill:var(--icon)"><use href="#i-bell" width="20" height="24" y="2"/><circle cx="17" cy="6" r="3" fill="var(--accent)"/></svg>
    </span>
    <span class="header-avatar" role="img" aria-label="Profile photo of the signed-in user"></span>
  </header>

  <form class="card" style="top:136px;height:650px" aria-label="Habit information">
    <h2 class="form-title">Habit Information</h2>
    <div class="type-row">
      <span class="type-label">Type:</span>
      <span class="radio"><span class="radio-dot radio-dot--on"></span>Good</span>
      <span class="radio"><span class="radio-dot"></span>Bad</span>
    </div>
    <div class="field field--active" style="top:156px">
      <span class="field-legend">Name</span>Reading One Book a Week
    </div>
    <span class="section-label">Loop</span>
    <div class="field" style="top:269px;left:28px">Cue</div>
    <div class="field" style="top:339px;left:28px">Craving</div>
    <div class="field" style="top:408px;left:28px">Response</div>
    <div class="field" style="top:477px;left:28px">Reward</div>
    <span class="btn-primary">Add Habit</span>
  </form>

  <nav class="bottom-nav" style="top:818px">
    <svg class="nav-icon" style="left:36px;fill:var(--icon)" width="26" height="26"><use href="#i-compass"/></svg>
    <svg class="nav-icon" style="left:119px;fill:var(--icon)" width="20" height="26"><use href="#i-book"/></svg>
    <span class="nav-add" style="left:199px"><svg width="20" height="20" viewBox="0 0 20 20" stroke="#fff" stroke-width="2.4" stroke-linecap="round"><path d="M10 2v16M2 10h16"/></svg></span>
    <svg class="nav-icon" style="left:283px;fill:var(--icon)" width="26" height="24"><use href="#i-heart"/></svg>
    <svg class="nav-icon" style="left:363px;fill:var(--icon);color:var(--icon)" width="26" height="26"><use href="#i-gear"/></svg>
  </nav>
</section>

</body>
</html>
```